Tidewell Pronto Clinic Business card

We want a business card that matches our business theme. Our website is www.prontoclinicbz.example
The company name is Tidewell Pronto Clinic
The persons having the business cards will be doctors
My logo is attached.
We have a drive-thru medical center where our motto is Fast, Reliable, and Convenient. Our goal is to change the medical space while utilizing technologies, keeping a professional and clean look

Medical

Info on the card should be: Name, Position, Cell number, website, email address, possibly the office line as well

• Logo
• Professional medical feel with our logo colors incorporated

```html
<!DOCTYPE html>
<html lang="en">
<head>
<meta charset="utf-8">
<title>Tidewell Pronto Clinic — Business Card</title>
<link rel="stylesheet" href="https://fonts.googleapis.com/css2?family=Montserrat:wght@700&family=Didact+Gothic&display=swap">
<style>
  :root {
    --page-bg: #ececec;
    --card-white: #f4f4f4;
    --brand-blue: #1c47a0;
    --brand-blue-light: #2a5cb0;
    --accent-sky: #5ec8ef;
    --ink: #2b2b2b;
    --divider: #c9c9c9;
  }
  * { box-sizing: border-box; margin: 0; padding: 0; }
  html, body { width: 1156px; height: 1200px; overflow: hidden; }
  body {
    background: var(--page-bg);
    font-family: "Didact Gothic", sans-serif;
    color: var(--ink);
    position: relative;
  }
  .card {
    position: absolute;
    left: 148px;
    width: 860px;
    height: 492px;
    border-radius: 14px;
    box-shadow: 0 10px 30px rgba(0,0,0,0.12);
    overflow: hidden;
  }
  .card--front { top: 80px; background: var(--card-white); }
  .card--back {
    top: 630px;
    background: linear-gradient(135deg, var(--brand-blue) 0%, var(--brand-blue-light) 100%);
  }

  /* front */
  .brand-lockup {
    position: absolute;
    left: 70px;
    top: 200px;
    display: flex;
    align-items: center;
    gap: 16px;
  }
  .brand-lockup__name {
    font-family: "Didact Gothic", sans-serif;
    font-size: 30px;
    line-height: 1.1;
    color: var(--brand-blue);
    width: 210px;
  }
  .brand-lockup__dot {
    width: 76px; height: 76px;
    border-radius: 50%;
    background: var(--accent-sky);
    flex: none;
  }
  .divider {
    position: absolute;
    left: 448px;
    top: 118px;
    width: 2px;
    height: 242px;
    background: var(--divider);
  }
  .contact-block { position: absolute; left: 472px; top: 114px; }
  .contact-block__name {
    font-family: "Montserrat", sans-serif;
    font-weight: 700;
    font-size: 30px;
    color: var(--brand-blue);
    letter-spacing: 0.5px;
  }
  .contact-block__role { font-size: 21px; margin-top: 6px; }
  .contact-list { list-style: none; margin-top: 40px; }
  .contact-list li {
    display: flex; align-items: center; gap: 14px;
    font-size: 20px; height: 34px;
  }
  .contact-list svg { width: 20px; height: 20px; flex: none; fill: var(--brand-blue); }

  /* back */
  .world-texture {
    position: absolute; inset: 0;
    background: radial-gradient(ellipse at 55% 45%, rgba(255,255,255,0.07), rgba(255,255,255,0) 70%);
  }
  .back-lockup {
    position: absolute;
    left: 0; right: 0;
    top: 160px;
    display: flex; justify-content: center; align-items: center; gap: 22px;
  }
  .back-lockup__name {
    font-family: "Didact Gothic", sans-serif;
    font-size: 44px;
    line-height: 1.1;
    color: #ffffff;
    width: 300px;
  }
  .back-lockup__dot {
    width: 120px; height: 120px; border-radius: 50%;
    background: #ffffff; flex: none;
  }
  .tagline {
    position: absolute; left: 0; right: 0; top: 365px;
    text-align: center;
    font-size: 21px; color: #ffffff; letter-spacing: 1px;
  }
</style>
</head>
<body>

<section class="card card--front" aria-label="Card front">
  <div class="brand-lockup">
    <span class="brand-lockup__name">Tidewell Pronto Clinic</span>
    <span class="brand-lockup__dot"></span>
  </div>
  <div class="divider"></div>
  <div class="contact-block">
    <h1 class="contact-block__name">DANIEL REYES</h1>
    <p class="contact-block__role">General Manager</p>
    <ul class="contact-list">
      <li>
        <svg viewBox="0 0 20 20" aria-hidden="true"><path d="M6 1h8a1.5 1.5 0 0 1 1.5 1.5v15A1.5 1.5 0 0 1 14 19H6a1.5 1.5 0 0 1-1.5-1.5v-15A1.5 1.5 0 0 1 6 1zm0 2v12h8V3zm4 13a1 1 0 1 0 0 2 1 1 0 0 0 0-2z"/></svg>
        501 555 0142
      </li>
      <li>
        <svg viewBox="0 0 20 20" aria-hidden="true"><path d="M4 2l3 0 1.5 4-2 1.5a10 10 0 0 0 6 6l1.5-2 4 1.5v3A2 2 0 0 1 16 18C8.5 18 2 11.5 2 4a2 2 0 0 1 2-2z"/></svg>
        501 555 0142
      </li>
      <li>
        <svg viewBox="0 0 20 20" aria-hidden="true"><path d="M1 4h18v12H1zm2 2v.5l7 4.5 7-4.5V6zm0 3v5h14V9l-7 4.5z"/></svg>
        dan@prontoclinicbz.example
      </li>
      <li>
        <svg viewBox="0 0 20 20" aria-hidden="true"><path d="M10 1a9 9 0 1 0 0 18 9 9 0 0 0 0-18zm-1 2.2V7H6.2A7 7 0 0 1 9 3.2zm2 0A7 7 0 0 1 13.8 7H11zM3.3 9H8v2H3.3a7 7 0 0 1 0-2zm6.7 0h2v2H10zm4 0h2.7a7 7 0 0 1 0 2H14zM6.2 13H9v3.8A7 7 0 0 1 6.2 13zm4.8 0h2.8A7 7 0 0 1 11 16.8z"/></svg>
        www.prontoclinicbz.example
      </li>
    </ul>
  </div>
</section>

<section class="card card--back" aria-label="Card back">
  <div class="world-texture" role="img" aria-label="Faint dotted world map texture"></div>
  <div class="back-lockup">
    <span class="back-lockup__name">Tidewell Pronto Clinic</span>
    <span class="back-lockup__dot"></span>
  </div>
  <p class="tagline">FAST I RELIABLE I CONVENIENT</p>
</section>

</body>
</html>
```